Company Brochure - Recruitment Agency

We need a company brochure. We are a recruitment firm and we want to depict a professional, energetic and result oriented image. We would like our brochure to be in line with our logo design. A color filled and modern design will be a big plus.

We want the brochure to be smaller than a A4 size paper, elongated in shape with 3 pages on each side (see attached pics)
Updates

Reason: Need more designs to compare. Did not like the ones I received so far.

Target Market(s)

Big Corporations and Global Multinational companies

Industry/Entity Type

It Company

Requirements
Must have
• 6 long-sided Pages Design (with 3 Pages on each side)
• Page Measurement: 26cm x 14cm (for each page)
• Brochure Measurement: 26cm x 14 cm (when folded)
Nice to have
• Theme in line with our logo design.
• Project a fast, energetic and professional image.
Should not have
• Am open at this moment

```html
<!DOCTYPE html>
<html lang="en">
<head>
<meta charset="utf-8">
<title>BrightPath Recruiters – Trifold Brochure</title>
<link href="https://fonts.googleapis.com/css2?family=Open+Sans:ital,wght@0,400;0,600;0,700;1,400;1,700&display=swap" rel="stylesheet">
<style>
  :root {
    --green: #1e9b3e;
    --green-deep: #17843a;
    --green-light: #5cc14a;
    --paper: #ffffff;
    --ink: #333638;
    --grey: #6d6e71;
    --stage: #5f6368;
    --photo-a: #dfe6ee;
    --photo-b: #b9c7d8;
    --photo-c: #c9b6d6;
  }
  * { box-sizing: border-box; margin: 0; padding: 0; }
  html, body { width: 900px; height: 1200px; overflow: hidden; }
  body {
    background: var(--stage);
    font-family: "Open Sans", Arial, sans-serif;
    color: var(--ink);
    position: relative;
  }
  .panel {
    position: absolute;
    width: 280px;
    height: 520px;
    background: var(--paper);
    overflow: hidden;
  }
  .panel svg.art { position: absolute; inset: 0; width: 100%; height: 100%; }
  .front-cover { left: 310px; top: 40px; box-shadow: 0 10px 30px rgba(0,0,0,.35); }
  .spread {
    position: absolute;
    left: 30px; top: 640px;
    width: 840px; height: 520px;
    box-shadow: 0 10px 30px rgba(0,0,0,.35);
  }
  .spread .panel { top: 0; }
  .spread .process-panel { left: 0; }
  .spread .contact-panel { left: 280px; border-left: 1px solid #e4e4e4; border-right: 1px solid #e4e4e4; }
  .spread .cover-panel { left: 560px; }

  .brand {
    position: absolute;
    display: flex; align-items: center; gap: 7px;
    font-weight: 700; font-size: 17px; color: var(--green);
    white-space: nowrap;
  }
  .brand-dot { width: 14px; height: 14px; border-radius: 50%; background: var(--green-light); flex: none; }
  .cover .brand { top: 48px; left: 0; right: 0; justify-content: center; }

  .web-address {
    position: absolute; left: 0; right: 0; bottom: 26px;
    text-align: center; color: #fff; font-weight: 600; font-size: 15px;
    letter-spacing: .3px;
  }

  .process-copy {
    position: absolute; top: 22px; left: 16px; right: 16px;
    color: #fff;
  }
  .process-copy h2 { font-size: 14px; font-style: italic; font-weight: 700; margin-bottom: 5px; }
  .process-copy .intro { font-size: 8.5px; font-style: italic; line-height: 1.4; margin-bottom: 8px; }
  .process-steps { list-style: none; }
  .process-steps li {
    position: relative; padding-left: 15px;
    font-size: 8.2px; line-height: 1.4; margin-bottom: 6px;
  }
  .process-steps li::before {
    content: counter(step); counter-increment: step;
    position: absolute; left: 0; top: 1px;
    width: 10px; height: 10px; border-radius: 50%;
    background: #fff; color: var(--green);
    font-size: 7px; font-weight: 700; text-align: center; line-height: 10px;
  }
  .process-steps { counter-reset: step; }
  .process-steps strong { font-weight: 700; }

  .contact-block { position: absolute; top: 118px; left: 0; right: 0; text-align: center; }
  .contact-block h2 { font-size: 15px; font-style: italic; font-weight: 700; color: var(--ink); }
  .contact-block .swoosh { display: block; margin: 2px auto 10px; }
  .contact-list { list-style: none; font-size: 11px; color: var(--grey); }
  .contact-list li { margin-bottom: 4px; }
  .contact-list .icon { display: block; margin: 0 auto 3px; }
  .contact-panel .brand { top: 370px; left: 0; right: 0; justify-content: center; }
  .postal-address {
    position: absolute; top: 404px; left: 30px; right: 30px;
    text-align: center; font-size: 9.5px; line-height: 1.45; color: var(--grey);
  }
</style>
</head>
<body>

<!-- Front cover -->
<section class="panel cover front-cover">
  <svg class="art" viewBox="0 0 280 520" aria-hidden="false">
    <defs>
      <linearGradient id="handshake-tone-a" x1="0" y1="0" x2="1" y2="1">
        <stop offset="0" stop-color="var(--photo-a)"/>
        <stop offset=".55" stop-color="var(--photo-b)"/>
        <stop offset="1" stop-color="var(--photo-c)"/>
      </linearGradient>
    </defs>
    <g role="img" aria-label="Photo: recruiter shaking hands with a candidate in a bright office">
      <path d="M280,118 L175,118 C90,130 40,210 40,300 C40,380 80,430 130,455 L280,430 Z" fill="url(#handshake-tone-a)"/>
    </g>
    <path d="M168,112 C70,128 22,215 24,305 C26,385 70,440 120,462" fill="none" stroke="var(--green)" stroke-width="5"/>
    <path d="M0,425 C90,468 200,455 280,382 L280,520 L0,520 Z" fill="var(--green-light)"/>
    <path d="M0,440 C90,480 200,470 280,400 L280,520 L0,520 Z" fill="var(--green)"/>
    <path d="M60,470 C150,482 230,452 280,416" fill="none" stroke="#fff" stroke-width="3"/>
  </svg>
  <div class="brand"><span class="brand-dot"></span>BrightPath Recruiters</div>
  <p class="web-address">www.brightpathhire.com</p>
</section>

<!-- Open spread (outside) -->
<div class="spread">

  <section class="panel process-panel">
    <svg class="art" viewBox="0 0 280 520">
      <defs>
        <linearGradient id="team-tone" x1="0" y1="0" x2="1" y2="1">
          <stop offset="0" stop-color="#e9e4e0"/>
          <stop offset=".5" stop-color="#9a8f89"/>
          <stop offset="1" stop-color="#3c4352"/>
        </linearGradient>
      </defs>
      <rect width="280" height="520" fill="var(--green)"/>
      <path d="M0,318 C150,328 235,380 250,440 C258,470 252,500 244,520 L0,520 Z" fill="#fff"/>
      <path d="M0,326 C145,336 226,386 240,442" fill="none" stroke="var(--green-light)" stroke-width="4"/>
      <g role="img" aria-label="Photo: team of smiling professionals working together at a desk">
        <path d="M0,338 C138,348 214,396 226,448 C232,476 228,500 222,520 L0,520 Z" fill="url(#team-tone)"/>
      </g>
    </svg>
    <div class="process-copy">
      <h2>Our Recruitment Process:</h2>
      <p class="intro">By using our service for Permanent Recruitment, you gain access to our rigorous sourcing and screening process:</p>
      <ol class="process-steps">
        <li><strong>Search &amp; Select:</strong> Detailed research and sourcing from our own network, referrals and targeted campaigns to reach strong candidates quickly.</li>
        <li><strong>Candidate Review:</strong> Every profile is checked against your brief, with skills tests and structured interviews before any shortlist is shared.</li>
        <li><strong>Client Interviews:</strong> We arrange meetings, gather feedback from both sides and keep the process moving without delays for your team.</li>
        <li><strong>Offer &amp; Placement:</strong> We support salary talks, reference checks and contract details until your new hire signs and starts.</li>
        <li><strong>Aftercare:</strong> Our consultants follow up during the first months to make sure the placement is a lasting success for everyone.</li>
      </ol>
    </div>
  </section>

  <section class="panel contact-panel">
    <div class="contact-block">
      <h2>Contact us:</h2>
      <svg class="swoosh" width="150" height="10" viewBox="0 0 150 10" aria-hidden="true">
        <path d="M2,8 C50,1 100,1 148,6" fill="none" stroke="var(--green)" stroke-width="2"/>
      </svg>
      <ul class="contact-list">
        <li>
          <svg class="icon" width="11" height="11" viewBox="0 0 12 12" aria-hidden="true">
            <circle cx="6" cy="6" r="6" fill="var(--green)"/>
            <path d="M4,3 L5.2,3 L5.6,4.6 L4.9,5.2 C5.3,6.1 5.9,6.7 6.8,7.1 L7.4,6.4 L9,6.8 L9,8 C6,8.3 3.7,6 4,3 Z" fill="#fff"/>
          </svg>
          0100-555-0199
        </li>
        <li>
          <svg class="icon" width="11" height="11" viewBox="0 0 12 12" aria-hidden="true">
            <circle cx="6" cy="6" r="6" fill="var(--green)"/>
            <circle cx="6" cy="6" r="3" fill="none" stroke="#fff" stroke-width="1"/>
            <path d="M3,6 H9 M6,3 V9" stroke="#fff" stroke-width=".8"/>
          </svg>
          www.brightpathhire.com
        </li>
        <li>
          <svg class="icon" width="11" height="11" viewBox="0 0 12 12" aria-hidden="true">
            <circle cx="6" cy="6" r="6" fill="var(--green)"/>
            <rect x="3" y="4" width="6" height="4.2" fill="none" stroke="#fff" stroke-width=".9"/>
            <path d="M3,4 L6,6.4 L9,4" fill="none" stroke="#fff" stroke-width=".9"/>
          </svg>
          info@brightpathmail.com
        </li>
      </ul>
    </div>
    <div class="brand"><span class="brand-dot"></span>BrightPath Recruiters</div>
    <p class="postal-address">14, Lane 8, Maple Rd., Riverside Dist.,<br>Harbor City 210</p>
  </section>

  <section class="panel cover cover-panel">
    <svg class="art" viewBox="0 0 280 520">
      <defs>
        <linearGradient id="handshake-tone-b" x1="0" y1="0" x2="1" y2="1">
          <stop offset="0" stop-color="var(--photo-a)"/>
          <stop offset=".55" stop-color="var(--photo-b)"/>
          <stop offset="1" stop-color="var(--photo-c)"/>
        </linearGradient>
      </defs>
      <g role="img" aria-label="Photo: recruiter shaking hands with a candidate in a bright office">
        <path d="M280,118 L175,118 C90,130 40,210 40,300 C40,380 80,430 130,455 L280,430 Z" fill="url(#handshake-tone-b)"/>
      </g>
      <path d="M168,112 C70,128 22,215 24,305 C26,385 70,440 120,462" fill="none" stroke="var(--green)" stroke-width="5"/>
      <path d="M0,425 C90,468 200,455 280,382 L280,520 L0,520 Z" fill="var(--green-light)"/>
      <path d="M0,440 C90,480 200,470 280,400 L280,520 L0,520 Z" fill="var(--green)"/>
      <path d="M60,470 C150,482 230,452 280,416" fill="none" stroke="#fff" stroke-width="3"/>
    </svg>
    <div class="brand"><span class="brand-dot"></span>BrightPath Recruiters</div>
    <p class="web-address">www.brightpathhire.com</p>
  </section>

</div>
</body>
</html>
```